My business is primarily as a Herbalist, using Iridology to diagnose areas of weakness and which body systems need support and then dispensing a Herbal tonic. I also do Reflexology, Aromatherapy, Craniosacral Therapy, Reiki and make Organic Herbal Tea Blends.I don't have a logo. I will also be needing to update my business cards soon, but firstly need labels for a new product I've devised - CLEAR MIND BREW.This tea is powdered and is a combination of 16 herbs which help to nourish the brain tissues & support circulation to the brain, helping to prevent & prolong Dementia while also improving energy & vitality.My business colour is Magenta. My name is Delia Voskaridou, so maybe just use DELIA on the label.Please print address & mobile at the base of the label.81 Tulloch Rd Srathfield 2135 NSW | 0438172604 | The label needs to be round & no larger than 6cm

Target Market(s)

Universal

Industry/Entity Type

Health And Wellness

Font styles to use
Serif

Colors
6b449b
a64599

Requirements
Must have
• Magenta colour as a background.This colour is my so called trademark.
• DELIA- as a logo
• I want some vintage designs of florals with modern design.
• ORGANIC Herbal TEA blends
• CLEAR MIND BREW
• 200g
• Address & mobile at the base of label
Nice to have
• An improvement to my business card design & outlay.
• I love vintage but I also want it current. Sophisticated & stylish.
• It needs to represent quality & longevity & trust.

```html
<!DOCTYPE html>
<html lang="en">
<head>
<meta charset="utf-8">
<title>Clear Mind Brew – Round Label</title>
<link rel="stylesheet" href="https://fonts.googleapis.com/css2?family=Noto+Serif:wght@400;700&family=Roboto+Slab:wght@400&display=swap">
<style>
  :root {
    --page-bg: #f5f5f5;
    --rim: #7e1a47;
    --magenta: #c11767;
    --tab: #b3185e;
    --cream: #f8f7df;
    --olive: #6d6a26;
    --lavender: #b9a6de;
    --leaf: #b9c98a;
    --ink-light: #fbeef3;
  }
  html, body {
    margin: 0;
    width: 1200px;
    height: 885px;
    overflow: hidden;
    background: var(--page-bg);
  }
  .label {
    display: block;
    width: 1200px;
    height: 885px;
  }
  .label-rim { fill: var(--rim); }
  .label-field { fill: var(--magenta); }
  .label-cream { fill: var(--cream); }
  .brand-tab { fill: var(--tab); }
  .brand-name {
    font-family: "Noto Serif", serif;
    font-weight: 400;
    font-size: 34px;
    fill: var(--ink-light);
  }
  .product-title {
    font-family: "Noto Serif", serif;
    font-weight: 700;
    font-size: 66px;
    fill: var(--olive);
    letter-spacing: 1px;
  }
  .product-sub {
    font-family: "Noto Serif", serif;
    font-weight: 400;
    font-size: 35px;
    fill: var(--ink-light);
    letter-spacing: 1px;
  }
  .product-rule { stroke: var(--ink-light); stroke-width: 1.5; }
  .contact {
    font-family: "Roboto Slab", serif;
    font-weight: 400;
    font-size: 22px;
    fill: var(--ink-light);
  }
</style>
</head>
<body>
<svg class="label" viewBox="0 0 1200 885" xmlns="http://www.w3.org/2000/svg">
  <defs>
    <clipPath id="label-inner">
      <circle cx="600" cy="442" r="360"/>
    </clipPath>
    <radialGradient id="floral-left" cx="0.5" cy="0.5" r="0.5">
      <stop offset="0" stop-color="#c8b6e6"/>
      <stop offset="0.6" stop-color="#d9dcc0" stop-opacity="0.7"/>
      <stop offset="1" stop-color="#f8f7df" stop-opacity="0"/>
    </radialGradient>
    <radialGradient id="floral-right" cx="0.5" cy="0.5" r="0.5">
      <stop offset="0" stop-color="#c2afe3"/>
      <stop offset="0.6" stop-color="#d6dcbc" stop-opacity="0.7"/>
      <stop offset="1" stop-color="#f8f7df" stop-opacity="0"/>
    </radialGradient>
  </defs>

  <circle class="label-rim" cx="600" cy="442" r="382"/>
  <circle class="label-field" cx="600" cy="442" r="360"/>

  <g clip-path="url(#label-inner)">
    <rect class="label-cream" x="240" y="60" width="720" height="383"/>
    <g role="img" aria-label="Vintage watercolour florals of lilac blossoms, leaves and sprigs">
      <ellipse cx="330" cy="330" rx="140" ry="150" fill="url(#floral-left)"/>
      <ellipse cx="870" cy="330" rx="140" ry="150" fill="url(#floral-right)"/>
      <ellipse cx="470" cy="140" rx="110" ry="60" fill="url(#floral-left)"/>
      <ellipse cx="740" cy="140" rx="110" ry="60" fill="url(#floral-right)"/>
    </g>
  </g>

  <rect class="brand-tab" x="513" y="94" width="176" height="54"/>
  <text class="brand-name" x="601" y="133" text-anchor="middle">Delia</text>

  <text class="product-title" x="600" y="255" text-anchor="middle">CLEAR</text>
  <text class="product-title" x="600" y="335" text-anchor="middle">MIND</text>
  <text class="product-title" x="600" y="415" text-anchor="middle">BREW</text>

  <text class="product-sub" x="600" y="547" text-anchor="middle">ORGANIC Herbal</text>
  <text class="product-sub" x="600" y="591" text-anchor="middle">TEA blends</text>
  <line class="product-rule" x1="528" y1="605" x2="672" y2="605"/>
  <text class="product-sub" x="600" y="641" text-anchor="middle">200g</text>

  <text class="contact" x="600" y="719" text-anchor="middle">81 Tulloch Rd Srathfield 2135 NSW</text>
  <text class="contact" x="600" y="755" text-anchor="middle">0438172604</text>
</svg>
</body>
</html>
```